Construction company focused on concrete and shed construction.

We need to update our current business card for brindlebuilds.com.au we would like an eye catching design with blue, grey and white incorporating our current logo.
Our company started off in concreting and due to varying factors we have expanded to include shed construction as well.
This has led to our current Logo looking a little out of place and somehow need to use the card to bring in the shed construction side of the business while not having to change current concrete look "BRINDLE" logo as we already have this incorporated into our company clothing and are not willing to change this yet.
Photo image attached for inspiration/ visual reference of type of work, not to be used on final design.
Please no cheesy designs of men in hard hats and tools
Final design should demonstrate a modern and service focused company.

Target Market(s)

Farmers, Business owners, Developers, Architects, Commercial project delivery

Industry/Entity Type

Construction Company

Contact Information for Business Card

Brindle Builds.
7c Harcourt st
Kelsey Vale Tas
03 62918730

Font styles to use
Other font styles liked:
• see font in logo

Colors
3176b5
b2b2b2

Requirements
Must have
• Easy to read font,
• good contrast between back ground and writing
Nice to have
• Modern and corporate look with a fun but professional image.
Should not have
• Comic images or shadow images of tools/ people.

```html
<!DOCTYPE html>
<html lang="en">
<head>
<meta charset="utf-8">
<title>Brindle Builds – Business Card</title>
<link href="https://fonts.googleapis.com/css2?family=Montserrat:wght@600;700&family=Roboto:wght@400;500&display=swap" rel="stylesheet">
<style>
  :root {
    --brand-blue: #3176b5;
    --brand-grey: #b2b2b2;
    --ink-grey: #535a60;
    --text-grey: #4a4f54;
    --soft-grey: #8b8f93;
    --card-white: #efefef;
    --backdrop: #d9d6d1;
  }
  * { box-sizing: border-box; margin: 0; padding: 0; }
  html, body { width: 1200px; height: 545px; overflow: hidden; }
  body {
    background: var(--backdrop);
    font-family: "Roboto", Arial, sans-serif;
    position: relative;
  }
  .card {
    position: absolute;
    top: 117px;
    width: 510px;
    height: 298px;
    background: var(--card-white);
    overflow: hidden;
  }
  .card--front { left: 68px; border-radius: 26px 26px 26px 0; }
  .card--back { left: 618px; border-radius: 26px 26px 0 26px; }

  .brand-mark { position: absolute; display: flex; flex-direction: column; align-items: center; }
  .brand-mark__dot { border-radius: 50%; background: var(--brand-blue); }
  .brand-mark__name {
    font-family: "Montserrat", Arial, sans-serif;
    font-weight: 700;
    color: var(--ink-grey);
    letter-spacing: 1px;
    line-height: 1;
  }
  .card--front .brand-mark { left: 52px; top: 30px; width: 170px; }
  .card--front .brand-mark__dot { width: 150px; height: 150px; }
  .card--front .brand-mark__name { font-size: 20px; margin-top: 8px; }
  .card--back .brand-mark { left: -10px; top: 40px; width: 220px; }
  .card--back .brand-mark__dot { width: 200px; height: 200px; }
  .card--back .brand-mark__name { font-size: 24px; margin-top: 10px; }

  .divider {
    position: absolute; left: 261px; top: 35px;
    width: 1px; height: 113px; background: var(--brand-blue);
  }
  .wordmark { position: absolute; }
  .wordmark__name {
    font-family: "Montserrat", Arial, sans-serif;
    font-weight: 700;
    color: var(--brand-blue);
    line-height: 1;
    letter-spacing: 0.5px;
  }
  .wordmark__sub {
    font-family: "Montserrat", Arial, sans-serif;
    font-weight: 600;
    color: var(--ink-grey);
    letter-spacing: 2.5px;
    line-height: 1;
  }
  .wordmark__tagline { color: var(--soft-grey); line-height: 1; }
  .card--front .wordmark { left: 274px; top: 32px; }
  .card--front .wordmark__name { font-size: 42px; }
  .card--front .wordmark__sub { font-size: 18px; margin-top: 1px; }
  .card--front .wordmark__tagline { font-size: 13px; margin-top: 3px; }
  .card--back .wordmark { left: 252px; top: 108px; }
  .card--back .wordmark__name { font-size: 44px; }
  .card--back .wordmark__sub { font-size: 20px; margin-top: 1px; }
  .card--back .wordmark__tagline { font-size: 14px; margin-top: 3px; }

  .address {
    position: absolute; left: 274px; top: 118px;
    font-size: 14px; line-height: 18px; color: var(--text-grey); font-style: normal;
  }
  .contact { position: absolute; left: 44px; top: 230px; }
  .contact__name {
    font-family: "Montserrat", Arial, sans-serif;
    font-weight: 700; font-size: 17px; color: var(--ink-grey); letter-spacing: 0.5px;
  }
  .contact__role { font-size: 13px; color: var(--brand-blue); font-weight: 400; font-family: "Roboto", Arial, sans-serif; letter-spacing: 0; }
  .contact__phone { font-size: 13px; color: var(--text-grey); margin-top: 4px; }

  .services { position: absolute; left: 252px; top: 204px; list-style: none; }
  .services li {
    display: flex; align-items: center; gap: 8px;
    font-size: 13px; line-height: 20px; color: var(--text-grey);
  }
  .services svg { width: 9px; height: 8px; flex: none; }
</style>
</head>
<body>
  <section class="card card--front">
    <div class="brand-mark">
      <span class="brand-mark__dot"></span>
      <span class="brand-mark__name">BRINDLE</span>
    </div>
    <span class="divider"></span>
    <div class="wordmark">
      <div class="wordmark__name">BRINDLE</div>
      <div class="wordmark__sub">BUILDS</div>
      <div class="wordmark__tagline">Concrete and shed construction</div>
    </div>
    <address class="address">7c Harcourt st<br>Kelsey Vale Tas</address>
    <div class="contact">
      <div class="contact__name">MARCUS HALE <span class="contact__role">/ Managing director</span></div>
      <div class="contact__phone">P: 03 62918730</div>
    </div>
  </section>

  <section class="card card--back">
    <div class="brand-mark">
      <span class="brand-mark__dot"></span>
      <span class="brand-mark__name">BRINDLE</span>
    </div>
    <div class="wordmark">
      <div class="wordmark__name">BRINDLE</div>
      <div class="wordmark__sub">BUILDS</div>
      <div class="wordmark__tagline">Concrete and shed construction</div>
    </div>
    <ul class="services">
      <li><svg viewBox="0 0 9 8" aria-hidden="true"><polygon points="4.5,0 9,8 0,8" fill="#535a60"/></svg>Excavations</li>
      <li><svg viewBox="0 0 9 8" aria-hidden="true"><polygon points="4.5,0 9,8 0,8" fill="#535a60"/></svg>Concreting</li>
      <li><svg viewBox="0 0 9 8" aria-hidden="true"><polygon points="4.5,0 9,8 0,8" fill="#535a60"/></svg>Commercial construction</li>
    </ul>
  </section>
</body>
</html>
```